FarBridge Webpage Look and feel re-design - Main page only

At FarBridge, we provide Video Streaming and Live Video Conferencing for the funeral industry. We currently have a fully functional website at www.farbridge-example.com, but we would like to change the look and feel to something simple, crisp and clean. A simple re-design of the .dwt file that can be applied to the entire site is all that is required. We are looking for ideas as to how to make it look clean, more technical and professional. We included a sample wireframe, BUT we are open to ideas of what YOU think would look good and professional! We also re-designed our logo for use on the site (uploaded) and simplified that. Bottom line, we need your artistic input - and the.dwt file modified to reflect this new look and feel. MUST be done in dreamweaver (have CC 2014) so modifications to the pages can be made on our end - no other formats please. Looking forward to your creativity! NOTE - winning designer will be given access to the site to make required modifications to the .dwt file...

Target Market(s)

Target Audience is Funeral Directors - we want the design simple and easy to navigate - most are between 30 - 65 North America based.

Industry/Entity Type

Industry

Font styles to use
Sans Serif

Requirements
Must have
• Must be somewhat easily navigable on a mobile device. Good contrast for wording, so it is easily read.
Nice to have
• Nice to have some original icons for our services such as in the wireframe...
Should not have
• Hard to read wording or clutter (such as our old site... Much too cluttered)

```html
<!DOCTYPE html>
<html lang="en">
<head>
<meta charset="utf-8">
<title>FarBridge – Video Casting Made Easy</title>
<link href="https://fonts.googleapis.com/css2?family=Arimo:ital,wght@0,400;0,700;1,400&family=Open+Sans:wght@300;400;800&display=swap" rel="stylesheet">
<style>
:root{
  --brand-blue:#135a85;
  --brand-teal:#0e6185;
  --ink-grey:#6b6b6b;
  --soft-grey:#ebebeb;
  --footer-bg:#3d3d3d;
  --footer-base:#333333;
  --footer-text:#bdbdbd;
  --white:#ffffff;
  --tick:#8cc63f;
}
*{margin:0;padding:0;box-sizing:border-box}
html,body{width:1006px;height:1200px;overflow:hidden;background:var(--white)}
body{position:relative;font-family:"Arimo",Arial,sans-serif;color:var(--ink-grey)}
.abs{position:absolute}

/* header */
.site-header{position:absolute;left:0;top:0;width:1006px;height:64px;background:var(--white);border-bottom:1px solid #e2e2e2}
.brand{left:144px;top:8px;height:48px;display:flex;align-items:center;gap:6px;font-size:13px;font-weight:700;color:var(--brand-blue);letter-spacing:.3px}
.brand-dot{width:34px;height:34px;border-radius:50%;background:#d8d8d8;flex:0 0 34px}
.main-nav .nav-item{position:absolute;top:0;height:64px;line-height:66px;font-size:11px;color:#666}
.nav-divider{position:absolute;top:0;width:1px;height:64px;background:#e2e2e2}
.caret{display:inline-block;margin-left:5px;border-left:3px solid transparent;border-right:3px solid transparent;border-top:3px solid #888;vertical-align:middle}
.login-btn{left:647px;top:22px;width:79px;height:22px;background:var(--brand-teal);color:var(--white);font-size:9px;display:flex;align-items:center;justify-content:center;gap:5px}
.social{top:21px;width:23px;height:23px;border-radius:50%;background:#cfcfcf}

/* hero */
.hero{left:0;top:64px;width:1006px;height:400px;background:linear-gradient(90deg,#050505 0%,#0b0b0b 40%,#1c1c1c 60%,#2a2320 80%,#0d0d0d 100%)}
.hero-title{left:132px;top:160px;font-family:"Open Sans",sans-serif;font-weight:800;font-size:21px;color:var(--white);letter-spacing:.3px}
.hero-sub{left:132px;top:199px;font-family:"Open Sans",sans-serif;font-weight:300;font-size:19px;color:var(--white)}
.play-btn{left:132px;top:246px;width:49px;height:49px;border-radius:7px;background:linear-gradient(#f4f4f4,#cfcfcf)}
.watch{left:193px;top:253px;font-family:"Open Sans",sans-serif;color:var(--white)}
.watch strong{display:block;font-weight:800;font-size:15px;letter-spacing:.3px}
.watch span{display:block;font-weight:400;font-size:16px;margin-top:1px}
.benefits{left:138px;top:314px;list-style:none;font-family:"Open Sans",sans-serif;font-size:12.5px;color:var(--white)}
.benefits li{height:28px;display:flex;align-items:center;gap:8px}
.slide-arrow{top:246px}

/* testimonial */
.testimonial{left:0;top:464px;width:1006px;height:129px;background:var(--soft-grey)}
.quote-mark{font-family:Georgia,serif;font-size:26px;color:#aaa}
.quote-text{left:170px;top:36px;width:600px;font-style:italic;font-size:13.5px;line-height:22px;color:#8a8a8a}
.quote-author{left:171px;top:87px;font-size:10.5px;color:var(--brand-blue)}

/* features */
.section-title{left:0;top:637px;width:1006px;text-align:center;font-size:19.5px;color:var(--brand-blue);letter-spacing:.2px}
.feature{top:692px;width:220px;text-align:center}
.feature svg{display:block;margin:0 auto;height:94px}
.feature h3{font-weight:400;font-size:14px;color:var(--brand-blue);margin-top:16px}
.feature p{font-size:10.5px;line-height:18px;color:#8a8a8a;margin-top:8px}

/* call to action */
.cta{left:0;top:902px;width:1006px;height:87px;background:var(--brand-teal)}
.cta-text{left:144px;top:35px;font-size:14px;color:var(--white)}
.cta-btn{left:637px;top:24px;width:219px;height:40px;border-radius:3px;border:1px solid #c9d2da;background:linear-gradient(#ffffff,#dde3e8);color:var(--brand-blue);font-size:12.5px;display:flex;align-items:center;justify-content:center}

/* footer */
.site-footer{left:0;top:989px;width:1006px;height:165px;background:var(--footer-bg)}
.footer-col{top:38px;width:150px}
.footer-col h4{font-weight:400;font-size:13px;color:var(--white);padding-bottom:9px;border-bottom:1px solid #666}
.footer-col ul{list-style:none;margin-top:9px}
.footer-col li{font-size:8.5px;color:var(--footer-text);height:19.3px;padding-left:1px}
.footer-brand{left:710px;top:34px;width:152px;height:90px}
.footer-brand svg{position:absolute;left:31px;top:0}
.footer-brand span{position:absolute;left:0;top:0;width:152px;line-height:90px;text-align:center;font-size:19px;font-weight:700;color:#9a9a9a}
.footer-base{left:0;top:1154px;width:1006px;height:46px;background:var(--footer-base);text-align:center;line-height:46px;font-size:8.5px;color:var(--footer-text)}
</style>
</head>
<body>

<header class="site-header">
  <div class="abs brand"><span class="brand-dot"></span>FarBridge</div>
  <nav class="main-nav">
    <span class="nav-divider" style="left:285px"></span>
    <span class="nav-item" style="left:308px">Services<i class="caret"></i></span>
    <span class="nav-divider" style="left:368px"></span>
    <span class="nav-item" style="left:388px">Community<i class="caret"></i></span>
    <span class="nav-divider" style="left:461px"></span>
    <span class="nav-item" style="left:481px">Company<i class="caret"></i></span>
    <span class="nav-divider" style="left:546px"></span>
    <span class="nav-item" style="left:566px">Contact</span>
    <span class="nav-divider" style="left:621px"></span>
  </nav>
  <div class="abs login-btn">
    <svg width="9" height="9" viewBox="0 0 10 10"><circle cx="5" cy="3" r="2.5" fill="#fff"/><path d="M0 10c0-3.5 2-5 5-5s5 1.5 5 5z" fill="#fff"/></svg>
    LOGIN »
  </div>
  <span class="abs social" style="left:742px"></span>
  <span class="abs social" style="left:773px"></span>
  <span class="abs social" style="left:806px"></span>
  <span class="abs social" style="left:838px"></span>
</header>

<section class="abs hero" role="img" aria-label="Photo of a videographer filming with a professional camcorder against a dark background">
</section>
<h1 class="abs hero-title">VIDEO CASTING MADE EASY!</h1>
<p class="abs hero-sub">Just One Button - Simply press to start and stop</p>
<div class="abs play-btn">
  <svg width="49" height="49" viewBox="0 0 49 49"><circle cx="24.5" cy="24.5" r="14" fill="#c9c9c9"/><circle cx="24.5" cy="24.5" r="11" fill="#e8e8e8"/><path d="M20 17l11 7.5L20 32z" fill="#d9262b"/></svg>
</div>
<div class="abs watch"><strong>WATCH A SHORT VIDEO</strong><span>to see how it works</span></div>
<ul class="abs benefits">
  <li><svg width="13" height="11" viewBox="0 0 13 11"><path d="M1 6l3.5 3.5L12 1" stroke="var(--tick)" stroke-width="2.2" fill="none"/></svg>No Computer Needed</li>
  <li><svg width="13" height="11" viewBox="0 0 13 11"><path d="M1 6l3.5 3.5L12 1" stroke="var(--tick)" stroke-width="2.2" fill="none"/></svg>Client’s Love it</li>
  <li><svg width="13" height="11" viewBox="0 0 13 11"><path d="M1 6l3.5 3.5L12 1" stroke="var(--tick)" stroke-width="2.2" fill="none"/></svg>New Revenue</li>
</ul>
<svg class="abs slide-arrow" style="left:63px" width="14" height="54" viewBox="0 0 14 54"><path d="M13 1L1 27l12 26" stroke="#777" fill="none"/></svg>
<svg class="abs slide-arrow" style="left:932px" width="14" height="54" viewBox="0 0 14 54"><path d="M1 1l12 26L1 53" stroke="#777" fill="none"/></svg>

<section class="abs testimonial">
  <span class="abs quote-mark" style="left:143px;top:16px">“</span>
  <blockquote class="abs quote-text">This is new exciting technology being brought to us by FarBridge and it is taking our profession into a new realm of service.</blockquote>
  <span class="abs quote-mark" style="left:768px;top:50px">”</span>
  <p class="abs quote-author">Daniel Hartley, General Manager, Maple Grove Funeral Homes Limited, Ontario, Canada</p>
</section>

<h2 class="abs section-title">THE VIDEO CASTING PLATFORM YOU WILL LOVE</h2>

<div class="abs feature" style="left:170px">
  <svg width="100" height="94" viewBox="0 0 100 94">
    <rect x="12" y="10" width="38" height="16" rx="4" fill="var(--brand-blue)"/>
    <rect x="54" y="10" width="18" height="16" rx="4" fill="var(--brand-blue)"/>
    <rect x="0" y="22" width="72" height="50" rx="7" fill="var(--brand-blue)"/>
    <rect x="10" y="40" width="32" height="7" fill="#fff"/>
    <path d="M72 46L98 26v48z" fill="var(--brand-blue)"/>
  </svg>
  <h3>Easy Stream</h3>
  <p>Full feature video casting for<br>funerals made easy</p>
</div>

<div class="abs feature" style="left:387px">
  <svg width="94" height="94" viewBox="0 0 94 94">
    <path d="M30 2l17 16 17-16" stroke="var(--brand-blue)" stroke-width="6" fill="none"/>
    <rect x="2" y="18" width="90" height="68" rx="10" fill="var(--brand-blue)"/>
    <rect x="10" y="26" width="62" height="52" rx="6" fill="#fff"/>
    <rect x="14" y="30" width="54" height="44" rx="4" fill="var(--brand-blue)"/>
    <path d="M34 42l14 10-14 10z" fill="#fff"/>
    <circle cx="82" cy="40" r="3" fill="#fff"/><circle cx="82" cy="52" r="3" fill="#fff"/><circle cx="82" cy="64" r="3" fill="#fff"/>
  </svg>
  <h3>Easy Presence</h3>
  <p>Participate in the ceremony even<br>if you cannot be there</p>
</div>

<div class="abs feature" style="left:608px">
  <svg width="72" height="94" viewBox="0 0 72 94">
    <path d="M14 60A30 30 0 1 1 58 60" stroke="var(--brand-blue)" stroke-width="7" fill="none"/>
    <path d="M24 50A17 17 0 1 1 48 50" stroke="var(--brand-blue)" stroke-width="7" fill="none"/>
    <circle cx="36" cy="36" r="8" fill="var(--brand-blue)"/>
    <path d="M28 48h16l-4 42a4 4 0 0 1-8 0z" fill="var(--brand-blue)"/>
  </svg>
  <h3>Easy Mobile</h3>
  <p>Video cast from anywhere with<br>a tablet or phone</p>
</div>

<section class="abs cta">
  <p class="abs cta-text">Let us provide you with an analysis of the revenue potential for your business.</p>
  <div class="abs cta-btn">Click here to contact us today</div>
</section>

<footer class="abs site-footer">
  <div class="abs footer-col" style="left:144px">
    <h4>Company</h4>
    <ul><li>Our Story</li><li>Press</li><li>Privacy Policy</li></ul>
  </div>
  <div class="abs footer-col" style="left:338px">
    <h4>Services</h4>
    <ul><li>Easy Stream</li><li>Easy Presence</li><li>Easy Mobile</li></ul>
  </div>
  <div class="abs footer-col" style="left:532px">
    <h4>Services</h4>
    <ul><li>Testimonials</li><li>Partners</li><li>Help</li></ul>
  </div>
  <div class="abs footer-brand">
    <svg width="90" height="90" viewBox="0 0 90 90"><circle cx="45" cy="45" r="45" fill="#6b6b6b"/></svg>
    <span>FarBridge</span>
  </div>
</footer>
<div class="abs footer-base">©2014. FarBridge. All rights reserved.</div>

</body>
</html>
```